Letterhead in Word Format

We are a small law firm in the Midwest. Our clientele is generally small business owners and companies.

We recently had a complete re-brand with a new logo, new letterhead, business cards, etc. However, the major issue now is that we cannot use the letterhead without physically ordering letterhead. Thus, invoices, and other items cannot be custom drafted.

We require custom letterhead in MICROSOFT WORD format. Our logo will be provided to you. And we will also provide a copy of the letterhead that was prepared.

We would like to see designs that are black and white, sophisticated, elegant, and generally professional. We prefer a traditional design with just a touch of contemporary.

Please do not submit any designs that are not Microsoft Word compatible.

EDIT: Please view the attached letterhead. The design must include the logo, name, address, fax, phone, email, and name of attorney.
Updates

Thank you all for submitting designs. I just wanted to quickly provide some feedback. I saw a few designs that had the logo at the bottom. Because there will be text with margins at 1" all around, it's not practical have the logo at the bottom. Also, designs with blocks of gray or black would cause our printer to bleed black onto the letterhead, so that is not practical as well.

If you have any comments, please feel free to leave me a message. Thank you.

Target Market(s)

Small business owners, companies, real estate investors and developers.

Industry/Entity Type

Small Business

Font styles to use
Script

Requirements
Must have
• Microsoft Word Format

```html
<!DOCTYPE html>
<html lang="en">
<head>
<meta charset="utf-8">
<title>The Harlan Law Firm — Letterhead</title>
<link rel="stylesheet" href="https://fonts.googleapis.com/css2?family=Gelasio:wght@400;700&display=swap">
<style>
  :root {
    --paper: #ffffff;
    --band: #d9d9d9;
    --band-edge: #cfcfcf;
    --ink: #3a3a3a;
    --ink-strong: #1f1f1f;
    --muted: #6a6a6a;
    --white: #ffffff;
    --accent-bar: #111111;
    --watermark: #ebebeb;
    --signature-tone: #cfcfcf;
  }
  * { box-sizing: border-box; margin: 0; padding: 0; }
  html, body { width: 853px; height: 1200px; overflow: hidden; background: var(--paper); }
  body { font-family: "Gelasio", Georgia, serif; color: var(--ink); }
  .sheet { position: relative; width: 853px; height: 1200px; overflow: hidden; }

  .masthead {
    position: absolute; left: 0; top: 0; width: 853px; height: 212px;
    background: linear-gradient(180deg, var(--band) 0%, var(--band-edge) 100%);
  }
  .masthead__bar {
    position: absolute; right: 0; top: 0; width: 12px; height: 92px; background: var(--accent-bar);
  }
  .firm-name {
    position: absolute; left: 112px; top: 96px;
    font-size: 40px; font-weight: 400; letter-spacing: 1px;
    color: var(--white); white-space: nowrap;
  }
  .contact {
    position: absolute; left: 604px; top: 18px; width: 220px;
    font-size: 10px; line-height: 13px; color: var(--ink);
  }
  .contact__name { text-align: right; font-weight: 700; letter-spacing: 1px; font-size: 11px; color: var(--ink-strong); }
  .contact__title { text-align: right; font-style: italic; color: var(--muted); margin-bottom: 8px; }
  .contact__row { display: grid; grid-template-columns: 56px 1fr; column-gap: 6px; margin-bottom: 5px; }
  .contact__row dt { text-align: right; font-weight: 700; }
  .contact__row dd { text-align: left; }

  .letter { position: absolute; left: 113px; top: 408px; width: 630px; font-size: 14.2px; line-height: 20.5px; }
  .letter__date { margin-bottom: 30px; }
  .letter__recipient { margin-bottom: 18px; line-height: 19px; }
  .letter__recipient strong { color: var(--ink-strong); }
  .letter__body p { margin-bottom: 20px; text-align: justify; }
  .letter__closing { margin-top: 42px; }
  .signature {
    width: 150px; height: 66px; margin-top: 14px; border-radius: 4px;
    background: linear-gradient(90deg, var(--signature-tone), #e8e8e8);
  }

  .footer-mark {
    position: absolute; right: -20px; bottom: 6px;
    font-size: 84px; letter-spacing: 6px; color: var(--watermark); white-space: nowrap;
  }
</style>
</head>
<body>
<div class="sheet">
  <header class="masthead">
    <span class="masthead__bar"></span>
    <h1 class="firm-name">THE HARLAN LAW FIRM</h1>
    <div class="contact">
      <p class="contact__name">MIRA L. OKAFOR</p>
      <p class="contact__title">Principal Attorney</p>
      <dl>
        <div class="contact__row"><dt>Address:</dt><dd>4820 W. Linden Ave<br>Maplewood, Illinois 60199</dd></div>
        <div class="contact__row"><dt>Phone:</dt><dd>(708) 555-0142</dd></div>
        <div class="contact__row"><dt>Fax:</dt><dd>(708) 555-0187</dd></div>
        <div class="contact__row"><dt>Web:</dt><dd>www.harlanlawfirm.com</dd></div>
        <div class="contact__row"><dt>Email:</dt><dd>mira@harlanlawfirm.com</dd></div>
      </dl>
    </div>
  </header>

  <main class="letter">
    <p class="letter__date">January 26, 2014</p>
    <p class="letter__recipient"><strong>Daniel Reyes</strong><br>General Manager<br>Crestline Holdings</p>
    <div class="letter__body">
      <p>Lorem ipsum dolor sit amet, consectetur adipiscing elit. Donec orci purus, luctus vitae dignissim eu, iaculis sed purus. Vivamus faucibus, ipsum nec aliquet viverra, leo mauris condimentum ligula, sit amet sagittis enim ligula quis arcu. Nam egestas tortor id nisi porttitor mattis. In tortor ante, ultricies in suscipit a, tempus non massa. Vivamus et auctor mi. Fusce vel massa nulla. Phasellus nec eros mauris, et scelerisque orci. Donec malesuada orci vitae nulla accumsan porta a id massa. Quisque accumsan iaculis magna sit amet fringilla. Maecenas consequat, magna eget tincidunt semper, odio nibh rutrum mi, id feugiat ante nisi eu risus. Vestibulum nunc orci, rhoncus a placerat in, ultricies in mi.</p>
      <p>Quisque scelerisque sagittis nulla at porttitor. Mauris a justo et tellus interdum tristique. Sed id augue vitae urna euismod commodo aliquet a quam. Pellentesque arcu velit, cursus et malesuada ut, rutrum nisi iaculis consequat et diam. Nullam erat sem, rhoncus id ullamcorper vitae, rhoncus et arcu. In ultricies ultricies nulla, ut rutrum nisi iaculis at. Donec eu magna a metus ornare faucibus. Fusce aliquet faucibus ultricies. Morbi semper, est id tincidunt gravida, sem arcu adipiscing lacus, ac bibendum nulla leo eu purus. Quisque nec diam sed risus consectetur accumsan quis quis nibh. Vestibulum id purus lorem.</p>
    </div>
    <p class="letter__closing">Ipsum dolor,</p>
    <div class="signature" role="img" aria-label="Handwritten signature of Daniel Ortiz"></div>
  </main>

  <div class="footer-mark" aria-hidden="true">THE HARLAN LAW</div>
</div>
</body>
</html>
```